High Tech Real Estate Startup needs a business card

We are developing an innovative real estate marketing product based around advanced search and virtual reality.

We talk to people, we need business cards.

Target Market(s)

The target market is technology professionals and realtors.

Contact Information for Business Card

The information to be included will include

Name
Title
Phone Number
E-mail Address
www.quelzo.com

It should use simple iconography for each one of those fields.

Font styles to use
Other font styles liked:
• Co, Jubilat, Avenir

Colors

Designer to choose colors to be used in the design.

Requirements
Must have
• Clean aesthetic,
• Good use of negative space.
• It should use our company logo, shown in the attached file. It is able to use the negative of that logo (coloured font and white background) and I have attached other acceptable accent colours in a swatch file.
Should not have
• Should not be too busy
• No extraneous text (slogans, tag lines etc)

```html
<!DOCTYPE html>
<html lang="en">
<head>
<meta charset="utf-8">
<title>Quelzo Business Card</title>
<link rel="stylesheet" href="https://fonts.googleapis.com/css2?family=Mulish:wght@400;600&display=swap">
<style>
  :root {
    --canvas-bg: #2b2b2d;
    --card-black: #161618;
    --card-edge: #222225;
    --gloss-logo: #3a3a3e;
    --teal: #3cc3c4;
    --teal-deep: #2aa9ab;
    --foot-grey: #2c2c30;
    --text-light: #d8dadb;
    --white: #ffffff;
  }
  * { margin: 0; padding: 0; box-sizing: border-box; }
  html, body {
    width: 800px; height: 1200px; overflow: hidden;
    background: var(--canvas-bg);
    font-family: "Mulish", "Avenir", sans-serif;
  }
  .stage {
    position: relative; width: 800px; height: 1200px;
    display: flex; flex-direction: column; align-items: center; justify-content: center;
    gap: 110px;
  }
  .card {
    position: relative; width: 640px; height: 366px;
    background: var(--card-black);
    border-radius: 22px;
    border: 1px solid var(--card-edge);
    overflow: hidden;
  }
  /* Front */
  .card-front .wordmark {
    position: absolute; inset: 0;
    display: flex; align-items: center; justify-content: center;
    font-weight: 600; font-size: 78px; letter-spacing: 4px;
    color: var(--gloss-logo);
  }
  /* Back */
  .card-back .wordmark {
    position: absolute; left: 48px; top: 118px;
    font-weight: 600; font-size: 50px; letter-spacing: 2px;
    color: var(--teal);
  }
  .contact {
    position: absolute; left: 352px; top: 124px;
  }
  .contact .name {
    font-weight: 600; font-size: 30px; color: var(--teal);
    margin-bottom: 16px;
  }
  .contact .line {
    display: flex; align-items: center; gap: 12px;
    font-size: 15px; color: var(--text-light);
    margin-bottom: 8px;
  }
  .contact .icon { width: 18px; height: 18px; flex: none; }
  .footer-band { position: absolute; left: 0; bottom: 0; width: 640px; height: 70px; }
  .footer-band .url {
    position: absolute; right: 0; bottom: 0; width: 470px; height: 48px;
    display: flex; align-items: center; justify-content: center;
    font-size: 15px; color: var(--white); letter-spacing: 0.5px;
  }
</style>
</head>
<body>
<main class="stage">
  <section class="card card-front">
    <div class="wordmark">QUELZO</div>
  </section>

  <section class="card card-back">
    <div class="wordmark">QUELZO</div>

    <div class="contact">
      <p class="name">Dana Reyes</p>
      <p class="line">
        <svg class="icon" viewBox="0 0 18 18">
          <circle cx="9" cy="9" r="9" fill="var(--teal)"/>
          <path d="M6.2 4.6l1.6 1.9-.9 1.2c.6 1.3 1.5 2.2 2.8 2.8l1.2-.9 1.9 1.6-.9 1.8c-3.5-.3-6.6-3.4-6.9-6.9z" fill="var(--card-black)"/>
        </svg>
        555.555.5555
      </p>
      <p class="line">
        <svg class="icon" viewBox="0 0 18 18">
          <circle cx="9" cy="9" r="9" fill="var(--teal)"/>
          <rect x="4.5" y="6" width="9" height="6.2" rx="0.8" fill="var(--card-black)"/>
          <path d="M4.8 6.3L9 9.4l4.2-3.1" stroke="var(--teal)" stroke-width="0.9" fill="none"/>
        </svg>
        dana@quelzo.com
      </p>
    </div>

    <div class="footer-band">
      <svg width="640" height="70" viewBox="0 0 640 70">
        <rect x="0" y="34" width="640" height="36" fill="var(--foot-grey)"/>
        <path d="M140 70 C165 70 168 22 200 22 L640 22 L640 70 Z" fill="var(--teal)"/>
      </svg>
      <div class="url">www.quelzo.com</div>
    </div>
  </section>
</main>
</body>
</html>
```